Consultant company (start up) needs a bold, yet simple web design

We need a we design for "K7P Ledger & Consulting". As our name implies we are a consultant firm helping companies with public sector business (tenders), but also helping the buyer side. We provide market research and reports, advice (legal and business) and hands-on-help with tender applications (projectleader; analysing critiera and texts, document reviews, etc). We have a rather uniqe position in our market with our mixed competences of branding and market communication, formal management systems, and public tenders.

We have a strong drive to make tender business simple for our clients: we will take care of the complicated!

We want our web design to be bold, yet clean and simple, communicating:

Competence; Commitment, Simplicity (for the customer).
Updates

Reason: For different reasons our web project was put on hold/was delayed a few days. As of today we are kicking life into it again, and expect to come back with feedback on designs in the next days. Best regards, Mattias

Target Market(s)

We primarily help companies aiming for public contracts.

Industry/Entity Type

Business Consultant

Contact Information for Business Card

Company logo; First name, Last name, Titel, webadress; personal e-mail
Maybe: a motto like "Offentliga affärer. Enklare" ("Public business. Made simple.")

Coding

Coded - Design and coding required

Font styles to use
Sans Serif

Colors

Designer to choose colors to be used in the design.

Requirements
Must have
• Dual language (Swedish and English)
• Responsive design, many people will view our webpage on their phone or tavlo.
• We want to make our position clear, stating what distinguishes us from "the rest of the pack" in maybe with on the starting page.
• [Will update brief; need to think this through]
Nice to have
• We have our logo in three colours. Green is our first. We are not yet sure why we have the different colurs. Maybe (just maybe!) the different colours can be put to use?
• We need help with the choice of images.
Should not have
• Never boring.

```html
<!DOCTYPE html>
<html lang="en">
<head>
<meta charset="utf-8">
<title>K7P Ledger &amp; Consulting</title>
<link rel="stylesheet" href="https://fonts.googleapis.com/css2?family=Exo+2:wght@500;600&family=Open+Sans:wght@400;600&display=swap">
<style>
  :root {
    --frame: #e5e5e5;
    --page: #ffffff;
    --brand: #0a7cc4;
    --brand-deep: #006384;
    --nav: #0d6a8e;
    --nav-active: #7cc3dc;
    --ink: #333333;
    --ink-soft: #444444;
    --footer-link: #d8eef6;
  }
  * { margin: 0; padding: 0; box-sizing: border-box; }
  html, body { width: 1200px; height: 1200px; overflow: hidden; background: var(--frame); }
  body { position: relative; font-family: "Open Sans", Arial, sans-serif; color: var(--ink); }
  .page { position: absolute; left: 14px; top: 14px; width: 1172px; height: 1172px; background: var(--page); }

  .brand { position: absolute; display: flex; align-items: center; gap: 10px;
           font-family: "Exo 2", Arial, sans-serif; font-weight: 600; font-size: 22px; line-height: 24px; }
  .brand__dot { width: 30px; height: 30px; border-radius: 50%; background: var(--brand); flex: none; }
  .brand__name { display: block; white-space: nowrap; }
  .brand--header { left: 52px; top: 40px; color: var(--ink); }
  .brand--footer { left: 0; right: 0; top: 36px; justify-content: center; color: #fff; }
  .brand--footer .brand__dot { background: #fff; }

  .main-nav { position: absolute; left: 337px; top: 60px; display: flex; gap: 25px; line-height: 20px;
              font-family: "Exo 2", Arial, sans-serif; font-weight: 500; font-size: 16px; }
  .main-nav a { color: var(--nav); text-decoration: none; }
  .main-nav a.is-active { color: var(--nav-active); }

  .contact { position: absolute; top: 60px; height: 21px; display: flex; align-items: center; gap: 6px;
             font-family: "Exo 2", Arial, sans-serif; font-weight: 500; font-size: 14px; color: #333; }
  .contact svg { width: 21px; height: 21px; }
  .contact--phone { left: 803px; }
  .contact--mail { left: 938px; }

  .hero { position: absolute; left: 51px; top: 134px; width: 1071px; height: 415px;
          background: linear-gradient(100deg, #c9ccd0 0%, #e9ecf0 25%, #b7c7dc 55%, #e3e9f1 80%, #f4f6f9 100%); }

  .section-title { position: absolute; top: 609px; font-family: "Exo 2", Arial, sans-serif;
                   font-weight: 600; font-size: 20px; line-height: 26px; color: var(--brand); letter-spacing: 0.3px; }
  .about-title { left: 53px; }
  .services-title { left: 635px; }

  .body-copy { position: absolute; top: 676px; font-size: 13.4px; line-height: 19.9px; color: var(--ink-soft); white-space: nowrap; }
  .about-copy { left: 53px; }
  .services-copy { left: 833px; }

  .services-visual { position: absolute; left: 632px; top: 674px; width: 180px; height: 180px;
                     background: linear-gradient(135deg, #2b4c78 0%, #5d86b8 50%, #a9c8e6 100%);
                     box-shadow: 0 8px 8px -6px rgba(0,0,0,0.35); }

  .button { position: absolute; top: 881px; height: 37px; border-radius: 3px; background: var(--brand);
            color: #fff; font-weight: 600; font-size: 15px; letter-spacing: -0.2px;
            display: flex; align-items: center; justify-content: center; text-decoration: none; }
  .button--about { left: 54px; width: 216px; }
  .button--services { left: 834px; width: 164px; }

  .site-footer { position: absolute; left: 0; top: 964px; width: 1172px; height: 176px; background: var(--brand-deep); }
  .footer-rule { position: absolute; left: 337px; top: 107px; width: 498px; height: 1px; background: rgba(255,255,255,0.75); }
  .footer-nav { position: absolute; left: 0; right: 0; top: 124px; display: flex; justify-content: center; gap: 21px;
                font-family: "Exo 2", Arial, sans-serif; font-weight: 500; font-size: 14px; line-height: 20px; }
  .footer-nav a { color: var(--footer-link); text-decoration: none; }
  .footer-nav a.is-active { color: var(--nav-active); }

  .copyright { position: absolute; left: 0; right: 0; top: 1146px; text-align: center;
               font-size: 11px; line-height: 16px; font-weight: 600; color: #333; }
</style>
</head>
<body>
<div class="page">
  <header>
    <div class="brand brand--header"><span class="brand__dot"></span><span><span class="brand__name">K7P Ledger &amp;</span><span class="brand__name">Consulting</span></span></div>
    <nav class="main-nav">
      <a href="#" class="is-active">Home</a><a href="#">About</a><a href="#">Services</a><a href="#">News</a><a href="#">Contact</a>
    </nav>
    <div class="contact contact--phone">
      <svg viewBox="0 0 22 22"><circle cx="11" cy="11" r="10" fill="none" stroke="#0d6a8e" stroke-width="1.8"/><path d="M7.5 6.5c.6-.6 1.3-.5 1.7.1l.9 1.4c.3.5.2 1-.2 1.4l-.5.5c.5 1.2 1.6 2.4 2.8 2.9l.5-.5c.4-.4.9-.5 1.4-.2l1.4.9c.6.4.7 1.1.1 1.7l-.7.7c-.9.9-3.4.1-5.5-2s-2.9-4.6-2-5.5z" fill="#0d6a8e"/></svg>
      040 7654321
    </div>
    <div class="contact contact--mail">
      <svg viewBox="0 0 22 22"><circle cx="11" cy="11" r="10" fill="none" stroke="#0d6a8e" stroke-width="1.8"/><rect x="6" y="7.5" width="10" height="7" rx="1" fill="none" stroke="#0d6a8e" stroke-width="1.5"/><path d="M6.5 8l4.5 3.5L15.5 8" fill="none" stroke="#0d6a8e" stroke-width="1.5"/></svg>
      info@k7pledger.com
    </div>
  </header>

  <div class="hero" role="img" aria-label="Photo of two consultants reviewing a tablet in a bright office"></div>

  <main>
    <h2 class="section-title about-title">ABOUT US</h2>
    <p class="body-copy about-copy">Lorem ipsum dolor sit amet, consectetuer adipiscing elit, sed diam nonummy nibh<br>euismod tincidunt ut laoreet dolore magna aliquam erat volutpat. Ut wisi enim ad<br>minim veniam, quis nostrud exerci tation ullamcorper suscipit lobortis nisl ut aliquip<br>ex ea commodo consequat. Duis autem vel eum iriure dolor in hendrerit in vulputate<br>velit esse molestie consequat, vel illum dolore eu feugiat nulla facilisis at vero eros<br>et accumsan et iusto odio dignissim qui blandit praesent luptatum zzril delenit augue<br>duis dolore te feugait nulla facilisi. Nam liber tempor cum soluta nobis eleifend option<br>congue nihil imperdiet doming id quod mazim placerat facer possim assum. Typi non<br>habent claritatem insitam; est usus legentis in iis qui facit eorum claritatem.</p>
    <a href="#" class="button button--about">MORE ABOUT K7P</a>

    <h2 class="section-title services-title">OUR SERVICES</h2>
    <div class="services-visual" role="img" aria-label="Image of a businessman holding a glowing digital globe with network and chart graphics"></div>
    <p class="body-copy services-copy">Lorem ipsum dolor sit amet, consectetuer adipis<br>euismod tincidunt ut laoreet dolore magna aliqu<br>minim veniam, quis nostrud exerci tation ullam<br>ex ea commodo consequat. Duis autem vel eum<br>velit esse molestie consequat, vel illum dolore eu<br>et accumsan et iusto odio dignissim qui blandit<br>duis dolore te feugait nulla facilisi. Nam liber te<br>congue nihil imperdiet doming id quod mazim<br>habent claritatem insitam; est usus legentis.</p>
    <a href="#" class="button button--services">DISCOVER MORE</a>
  </main>

  <footer class="site-footer">
    <div class="brand brand--footer"><span class="brand__dot"></span><span><span class="brand__name">K7P Ledger &amp;</span><span class="brand__name">Consulting</span></span></div>
    <div class="footer-rule"></div>
    <nav class="footer-nav">
      <a href="#" class="is-active">Home</a><a href="#">About</a><a href="#">Services</a><a href="#">News</a><a href="#">Contact</a>
    </nav>
  </footer>
  <p class="copyright">© 2017 K7P LEDGER AND CONSULTING. ALL RIGHTS RESERVED.</p>
</div>
</body>
</html>
```